Local jobs for students, local vendor post jobs, register users (students) receive notification

I need a simple app design for local shops to post jobs, register users (students) will then receive notifications base on their location (district...)

University students and local shops (flower, coffee, restaurant, etc.)

• Open up app:
• Page 1: Show 2 buttons: View recent jobs and Post a New Jobs
• Login/Registration pages
• Page 2: User registration (Name, Email, Phone and Login with Lumora)
• Page 3: User selection - Students or Local Shops
• Page 3a: If students - fill in the school name, select city, select districts that able to work, maximum 3 selection.
• Page 3b: If local shops - fill in the business name, select the business type (flower, coffee, restaurants, etc.), upload shop image, minimum 1 image maximum 3 images.
• Page 4a: Complete registration - View jobs button if student
• Page 4b: Complete registration - View post job button if vendors
• Signed in pages:
• On click view jobs button:
• Page 5a - Student - List of recent jobs (posted within 48 hours) with premium job display on top, list by most recent, small image of shop, short description, 3 lines of text, click an item to view more.
• Once click on item, show full contents (75 words maximum) with images, and a CALL NOW BUTTON
• On click post jobs button:
• Page 5b - Post job page - input job description in 50 words, select post type (free or premium)
• If premium select, payment type drop-down: show the description of the premium post (3 lines of texts), Credit Card payment inputs.
• Proceed to payment verification:
• Preview Post - Submit button
• DESIGN
• Font - Proxima Nova, Open Sans, Roboto (Unikey friendly, as the app will be in Vietnamese, will provide translation later)
• Style - Flat, Clean
• Color - Bold

```html
<!DOCTYPE html>
<html lang="en">
<head>
<meta charset="utf-8">
<title>Local Jobs – Recent Jobs</title>
<link rel="stylesheet" href="https://fonts.googleapis.com/css2?family=Roboto:wght@400;500&display=swap">
<style>
  :root {
    --backdrop: #efeded;
    --screen: #f7f8f9;
    --brand: #5a2a5c;
    --on-brand: #ffffff;
    --title: #1c1c1c;
    --meta: #a9a9ad;
    --divider: #e4e5e8;
    --thumb-empty: #e2e3e6;
  }
  * { box-sizing: border-box; margin: 0; padding: 0; }
  html, body {
    width: 1200px; height: 675px; overflow: hidden;
    background: var(--backdrop);
    font-family: "Roboto", sans-serif;
  }
  .canvas {
    width: 1200px; height: 675px;
    display: flex; align-items: center; justify-content: center;
  }
  .app-screen {
    width: 360px; height: 640px;
    background: var(--screen);
    overflow: hidden;
    box-shadow: 0 10px 30px rgba(60, 60, 80, 0.12);
  }
  .welcome-header {
    position: relative;
    height: 118px;
    background: var(--brand);
    color: var(--on-brand);
    display: flex; align-items: flex-end;
    padding: 0 18px 22px;
    gap: 12px;
  }
  .filter-button {
    position: absolute; top: 18px; right: 18px;
    width: 26px; height: 20px;
  }
  .avatar { width: 40px; height: 40px; flex: none; }
  .welcome-title { font-size: 20px; font-weight: 500; line-height: 1.2; }
  .welcome-subtitle { font-size: 11px; font-weight: 400; opacity: 0.95; margin-top: 2px; }
  .job-list { list-style: none; padding: 0 16px; }
  .job-item {
    display: flex; align-items: center; gap: 14px;
    height: 86px;
    border-bottom: 1px solid var(--divider);
  }
  .job-thumb {
    width: 86px; height: 54px; flex: none; border-radius: 2px;
  }
  .thumb-warehouse { background: linear-gradient(120deg, #b0552e 0%, #d9b08a 45%, #7b9ac4 100%); }
  .thumb-counter { background: linear-gradient(120deg, #c9a85a 0%, #e6dcc6 50%, #b8342e 100%); }
  .thumb-empty { background: var(--thumb-empty); }
  .job-title { font-size: 17px; font-weight: 500; color: var(--title); margin-bottom: 4px; }
  .job-meta { font-size: 12px; color: var(--meta); line-height: 1.35; }
</style>
</head>
<body>
<main class="canvas">
  <section class="app-screen">
    <header class="welcome-header">
      <svg class="filter-button" viewBox="0 0 26 20" aria-label="Filter jobs">
        <g stroke="#fff" stroke-width="2" stroke-linecap="round">
          <line x1="1" y1="3" x2="25" y2="3"/>
          <line x1="5" y1="10" x2="21" y2="10"/>
          <line x1="9" y1="17" x2="17" y2="17"/>
        </g>
      </svg>
      <svg class="avatar" viewBox="0 0 40 40" aria-label="User profile">
        <circle cx="20" cy="20" r="18.5" fill="none" stroke="#fff" stroke-width="2"/>
        <circle cx="20" cy="15" r="6" fill="#fff"/>
        <path d="M9 32c1.5-6 6-9 11-9s9.5 3 11 9" fill="#fff"/>
      </svg>
      <div class="welcome-text">
        <h1 class="welcome-title">Welcome John</h1>
        <p class="welcome-subtitle">Here some job based on your Location</p>
      </div>
    </header>
    <ul class="job-list">
      <li class="job-item">
        <div class="job-thumb thumb-warehouse" role="img" aria-label="Photo of a worker checking stock in a warehouse"></div>
        <div><h2 class="job-title">Inventory Associate</h2><p class="job-meta">Northvale Staffing - Inventory Associate - Part Time job in Cedar Hollow, CA</p></div>
      </li>
      <li class="job-item">
        <div class="job-thumb thumb-counter" role="img" aria-label="Photo of a shop assistant at a counter"></div>
        <div><h2 class="job-title">Cashier</h2><p class="job-meta">Northvale Staffing - Inventory Associate - Part Time job in Cedar Hollow, CA</p></div>
      </li>
      <li class="job-item">
        <div class="job-thumb thumb-warehouse" role="img" aria-label="Photo of a worker checking stock in a warehouse"></div>
        <div><h2 class="job-title">Restaurant Job</h2><p class="job-meta">Northvale Staffing - Inventory Associate - Part Time job in Cedar Hollow, CA</p></div>
      </li>
      <li class="job-item">
        <div class="job-thumb thumb-counter" role="img" aria-label="Photo of a shop assistant at a counter"></div>
        <div><h2 class="job-title">Cashier</h2><p class="job-meta">Northvale Staffing - Inventory Associate - Part Time job in Cedar Hollow, CA</p></div>
      </li>
      <li class="job-item">
        <div class="job-thumb thumb-warehouse" role="img" aria-label="Photo of a worker checking stock in a warehouse"></div>
        <div><h2 class="job-title">Job at Flowershop</h2><p class="job-meta">Northvale Staffing - Inventory Associate - Part Time job in Cedar Hollow, CA</p></div>
      </li>
      <li class="job-item">
        <div class="job-thumb thumb-empty" role="img" aria-label="Shop photo loading"></div>
        <div><h2 class="job-title">Account Manager</h2></div>
      </li>
    </ul>
  </section>
</main>
</body>
</html>
```